L & M Home Renovation & Repair business cards

L & M stands for pride and quality. I want the base color of card to be black and glossy. Double sided card with photos of some of my jobs on it. I need my phone number and email address on front as well. And I need a list of my services on back. -indoor outdoor repairs,- basement and bathroom remodels, -tile, laminate and hardwood flooring installation, -decks, fences, sheds and garages,-Windows and doors, -screen rooms,- trim work. I also need "No job to small....." on there.

Industry/Entity Type

Flooring

Contact Information for Business Card

I want something that catches the eye and shows some of my past work

Requirements
Must have
• FEEL FREE TO CHANGE IDEA IF YOU HAVE SOMETHING BETTER IN MIND. THANKS !!!!

```html
<!DOCTYPE html>
<html lang="en">
<head>
<meta charset="utf-8">
<title>L &amp; M Home Renovation &amp; Repair — Business Cards</title>
<link rel="stylesheet" href="https://fonts.googleapis.com/css2?family=Oswald:wght@300;400;500&display=swap">
<style>
  :root {
    --stage: #1b1b1b;
    --card-black: #050505;
    --card-grey: #3c3c3c;
    --ink: #f4f4f4;
    --ink-soft: #d9d9d9;
    --frame: #cfcfcf;
    --grass: #6f8a45;
    --sky: #a9bccb;
    --wood: #8a7456;
  }
  * { box-sizing: border-box; margin: 0; padding: 0; }
  html, body {
    width: 1200px; height: 800px; overflow: hidden;
    background: var(--stage);
    font-family: "Oswald", "Arial Narrow", sans-serif;
    color: var(--ink);
  }
  .stage {
    width: 1200px; height: 800px;
    display: flex; align-items: center; justify-content: center; gap: 40px;
  }
  .card {
    position: relative;
    width: 560px; height: 320px;
    overflow: hidden;
    background: linear-gradient(100deg, var(--card-grey) 0%, #1c1c1c 38%, var(--card-black) 62%);
    box-shadow: 0 18px 40px rgba(0,0,0,.55);
  }
  .card::after {
    content: "";
    position: absolute; inset: 0;
    background: linear-gradient(160deg, rgba(255,255,255,.10) 0%, rgba(255,255,255,0) 40%);
    pointer-events: none;
  }

  /* front */
  .brand { position: absolute; left: 40px; top: 28px; width: 180px; text-align: right; }
  .brand-name { font-size: 60px; font-weight: 400; line-height: 1; letter-spacing: 1px; }
  .brand-line { font-size: 11px; font-weight: 400; letter-spacing: .5px; margin-top: 6px; }
  .divider { position: absolute; left: 238px; top: 30px; width: 1px; height: 118px; background: var(--ink-soft); }
  .contact { position: absolute; left: 258px; top: 30px; }
  .contact-name { font-size: 30px; font-weight: 400; letter-spacing: 2px; line-height: 1.1; }
  .contact-title { font-size: 15px; font-weight: 300; margin: 4px 0 8px; }
  .contact-row { display: flex; align-items: center; gap: 7px; font-size: 12px; font-weight: 300; margin-top: 4px; }
  .contact-row svg { width: 11px; height: 11px; fill: var(--ink); }
  .work-row { position: absolute; left: 40px; top: 172px; display: flex; gap: 16px; }
  .work-thumb {
    width: 104px; height: 74px; border-radius: 14px;
    border: 2px solid var(--frame);
  }
  .thumb-floor { background: linear-gradient(135deg, #5a4a38, var(--wood)); }
  .thumb-tile { background: linear-gradient(135deg, #6d5f50, #a39480); }
  .thumb-yard { background: linear-gradient(180deg, var(--sky) 0%, #8a8a80 50%, var(--grass) 100%); }
  .thumb-deck { background: linear-gradient(180deg, #7f9bb4 0%, #8d7a5b 55%, #5f5038 100%); }
  .tagline {
    position: absolute; left: 40px; bottom: 22px;
    font-size: 18px; font-weight: 400; letter-spacing: 3px;
  }

  /* back */
  .gallery {
    position: absolute; left: 14px; top: 14px; width: 226px; height: 292px;
    display: grid; grid-template-columns: 1fr 1fr; grid-template-rows: 1fr 1fr; gap: 6px;
  }
  .gallery-shot { background: linear-gradient(180deg, var(--sky) 0%, #8c8d82 45%, var(--grass) 100%); }
  .gallery-shot.wide { grid-column: 1 / 3; background: linear-gradient(180deg, #b7c6d2 0%, #958c7e 45%, #5e7a3c 100%); }
  .gallery-shot.porch { background: linear-gradient(180deg, #9fb3c4 0%, #7d6b55 55%, #6a8641 100%); }
  .back-brand { position: absolute; right: 30px; top: 26px; text-align: right; }
  .back-brand .brand-name { font-size: 84px; }
  .back-brand .brand-line { font-size: 16px; font-weight: 500; margin-top: 8px; }
  .services {
    position: absolute; left: 252px; right: 20px; top: 176px;
    list-style: none; text-align: center;
    font-size: 13px; font-weight: 400; line-height: 1.5; color: var(--ink-soft);
  }
</style>
</head>
<body>
<main class="stage">

  <section class="card card-front" aria-label="Business card front">
    <div class="brand">
      <div class="brand-name">L &amp; M</div>
      <div class="brand-line">Home Renovation and Repair</div>
    </div>
    <div class="divider"></div>
    <div class="contact">
      <div class="contact-name">Your Name</div>
      <div class="contact-title">Job title</div>
      <div class="contact-row">
        <svg viewBox="0 0 24 24" aria-hidden="true"><path d="M6.6 10.8a15.1 15.1 0 0 0 6.6 6.6l2.2-2.2a1 1 0 0 1 1-.25 11.4 11.4 0 0 0 3.6.57 1 1 0 0 1 1 1V20a1 1 0 0 1-1 1A17 17 0 0 1 3 4a1 1 0 0 1 1-1h3.5a1 1 0 0 1 1 1c0 1.25.2 2.45.57 3.57a1 1 0 0 1-.25 1z"/></svg>
        <span>270-555-0148</span>
      </div>
      <div class="contact-row">
        <svg viewBox="0 0 24 24" aria-hidden="true"><path d="M2 5h20v14H2zm2 2v.5l8 5 8-5V7zm0 2.8V17h16V9.8l-8 5z"/></svg>
        <span>lmhomerenovation@mailbox.com</span>
      </div>
    </div>
    <div class="work-row">
      <div class="work-thumb thumb-floor" role="img" aria-label="Photo of a hardwood floor installation"></div>
      <div class="work-thumb thumb-tile" role="img" aria-label="Photo of a tiled floor with diamond inlay"></div>
      <div class="work-thumb thumb-yard" role="img" aria-label="Photo of a finished backyard project"></div>
      <div class="work-thumb thumb-deck" role="img" aria-label="Photo of a newly built deck"></div>
    </div>
    <div class="tagline">Labor &amp; Mastery at its Best</div>
  </section>

  <section class="card card-back" aria-label="Business card back">
    <div class="gallery">
      <div class="gallery-shot porch" role="img" aria-label="Photo of a covered porch build"></div>
      <div class="gallery-shot" role="img" aria-label="Photo of a brick house with new deck"></div>
      <div class="gallery-shot wide" role="img" aria-label="Photo of a screen room on a lawn"></div>
    </div>
    <div class="back-brand">
      <div class="brand-name">L &amp; M</div>
      <div class="brand-line">Home Renovation and Repair</div>
    </div>
    <ul class="services">
      <li>Indoor outdoor repairs</li>
      <li>basement and bathroom remodels,</li>
      <li>Tile, laminate and hardwood flooring installation</li>
      <li>Decks, Fences, Sheds and Garages</li>
      <li>Windows and doors, -screen rooms, - trim work</li>
    </ul>
  </section>

</main>
</body>
</html>
```